Consulting, Investors, Joint Venture Website

Founded in April 2018, Marendo Advisers Limited (MAL) is an advisory consulting firm specializing in engaging investors in business ventures in Tanzania.
With extensive experience in construction, energy, oil and gas and the legal professions, our team assembles our expertise that allows foreign investors to set foot and flourish in the Tanzanian market.
MAL is locally owned, founded and registered. Our shareholders are cultured Tanzanian citizens with extensive corporate experience in South Africa, Tanzania, United Kingdom and the United States.

Our mission is to provide responsive and unrivalled professional advice from learned and experienced professionals versed in the local market, with an understanding of the cultural and logistical challenges faced by foreign investors.

Our vision is to provide a complete investor’s package that initiates with company registration, compliance and documentation services and ultimately operational facilitation services.

Target Market(s)

Foreign Investors, International companies

Industry/Entity Type

Business Consultant

Number of Pages Required

5+ page

Requirements
Must have
• It will be 5 pages - Home, About Us, Services, Portfolio, Contact Us
Nice to have
• if it can look like https://www.vq-sample.com/
• or https://www.torvell.com or http://www.bramwickpoint.com/

```html
<!DOCTYPE html>
<html lang="en">
<head>
<meta charset="utf-8">
<title>Marendo Advisers – Home</title>
<link href="https://fonts.googleapis.com/css2?family=Raleway:wght@400;500;600;700&family=Roboto:wght@400;500;700&display=swap" rel="stylesheet">
<style>
:root{
  --blue:#0e4fa1;
  --blue-dark:#0a3f86;
  --blue-band:#1f5aa6;
  --orange:#f7941d;
  --white:#ffffff;
  --text:#2b3a55;
  --muted:#8a97b4;
  --line:#e4e9f2;
}
*{box-sizing:border-box;margin:0;padding:0}
html,body{width:1200px;height:3303px;overflow:hidden;background:var(--white)}
body{position:relative;font-family:"Raleway",sans-serif;color:var(--text)}
.abs{position:absolute}

/* header */
.site-header{left:0;top:0;width:1200px;height:105px;background:var(--white);z-index:3}
.brand{left:40px;top:30px;display:flex;align-items:center;gap:10px}
.brand-mark{width:34px;height:34px;background:var(--blue)}
.brand-name{font-weight:700;font-size:30px;color:var(--blue);letter-spacing:1px;line-height:1}
.nav-link{top:44px;font-size:14px;line-height:16px;color:var(--blue);font-weight:500;white-space:nowrap}
.nav-link.active{color:var(--orange);border-bottom:3px solid var(--orange);padding-bottom:12px}
.btn-contact-nav{left:676px;top:30px;width:136px;height:46px;border-radius:23px;background:var(--orange);color:var(--white);font-size:14px;display:flex;align-items:center;justify-content:center;font-weight:500}
.header-mail{left:825px;top:42px;display:flex;align-items:center;gap:10px;font-size:14px;color:var(--blue);font-weight:600;white-space:nowrap}
.social{left:1027px;top:38px;display:flex;gap:8px}
.social span{width:26px;height:26px;background:var(--blue);display:block}

/* hero */
.hero{left:0;top:105px;width:1200px;height:797px;background:linear-gradient(120deg,#e8dccb 0%,#f2e9dd 40%,#e9d7ba 60%,#b9c8d8 85%,#8fa9c4 100%)}
.hero-fade{left:0;top:105px;width:1200px;height:797px;background:linear-gradient(90deg,rgba(255,255,255,.45),rgba(255,255,255,.2) 50%,rgba(255,255,255,0))}
.hero-title{left:0;top:310px;width:1200px;text-align:center;font-size:58px;font-weight:600;color:var(--blue)}
.hero-text{left:270px;top:392px;width:660px;text-align:center;font-size:24px;line-height:32px;color:var(--blue);font-weight:500}
.btn{height:48px;border-radius:24px;display:flex;align-items:center;justify-content:center;font-size:15px}
.btn-outline{left:449px;top:507px;width:137px;border:2px solid var(--blue);color:var(--blue);background:transparent}
.btn-fill{left:612px;top:507px;width:137px;background:var(--orange);color:var(--white)}
.arrow{top:460px;width:50px;height:50px}

/* services */
.section-title{left:0;width:1200px;text-align:center;font-size:36px;font-weight:700;color:var(--blue)}
.section-title.light{color:var(--white)}
.service-card{top:818px;width:272px;height:469px;background:var(--white);box-shadow:0 3px 10px rgba(20,40,80,.18)}
.service-photo{width:272px;height:275px;display:block}
.service-name{margin-top:30px;text-align:center;color:var(--orange);font-size:17px;font-weight:500}
.service-text{margin:18px 18px 0;text-align:center;color:var(--muted);font-size:12.5px;line-height:17px}
.btn-more{left:524px;top:1329px;width:149px;height:46px;border:2px solid var(--blue);border-radius:23px;color:var(--blue);font-size:14px;display:flex;align-items:center;justify-content:center}

/* who we are */
.who-band{left:0;top:1412px;width:1200px;height:502px;background:linear-gradient(180deg,#1d5aa8,#2f6db4 60%,#1b4f92)}
.who-card{top:1518px;height:330px;background:var(--white);box-shadow:0 3px 10px rgba(0,0,0,.2)}
.who-head{height:70px;background:var(--blue);color:var(--white);font-size:23px;font-weight:600;display:flex;align-items:center;justify-content:center}
.who-text{padding:40px 18px 0;text-align:center;font-size:14px;line-height:25px;color:var(--blue)}

/* feedback */
.feedback-card{top:2039px;width:365px;height:436px;background:var(--white);box-shadow:0 3px 10px rgba(20,40,80,.2)}
.feedback-photo{width:365px;height:249px;display:block}
.quote{margin:22px 22px 0;text-align:center;font-family:"Roboto",sans-serif;font-weight:700;font-size:12.5px;line-height:16px;color:var(--text)}
.stars{display:flex;justify-content:center;gap:4px;margin-top:10px}
.person{margin-top:14px;text-align:center;font-family:"Roboto",sans-serif;font-size:13px;color:var(--text);line-height:17px}
.person em{display:block;color:#556}

/* contact */
.contact-band{left:0;top:2545px;width:1200px;height:608px;background:linear-gradient(180deg,#3e6ea9,#2d5c98 50%,#23508a)}
.form-panel{left:136px;top:2658px;width:597px;height:440px;background:var(--white);box-shadow:0 4px 14px rgba(0,0,0,.25)}
.form-title{left:53px;top:52px;font-size:24px;font-weight:600;color:var(--blue)}
.field{width:210px;border-bottom:1.5px solid var(--orange);padding-bottom:4px;font-size:12px;color:var(--muted)}
.send{left:430px;top:322px;width:104px;height:56px;background:var(--orange)}
.info-panel{left:733px;top:2658px;width:332px;height:440px;background:rgba(20,70,150,.88)}
.info-title{left:52px;top:52px;font-size:24px;font-weight:600;color:var(--white)}
.info-row{left:52px;display:flex;align-items:center;gap:20px;color:#dbe5f4;font-size:16px;line-height:22px}
.info-social{left:64px;top:362px;display:flex;gap:22px}
.info-social span{width:34px;height:34px;border:2px solid var(--white);display:block}

/* footer */
.footer-brand{left:0;top:3182px;width:1200px;display:flex;justify-content:center;align-items:center;gap:10px}
.copyright{left:0;top:3240px;width:1200px;text-align:center;font-size:16px;color:var(--blue)}
</style>
</head>
<body>

<header class="site-header abs">
  <div class="brand abs"><span class="brand-mark"></span><span class="brand-name">MARENDO</span></div>
  <nav>
    <span class="nav-link active abs" style="left:301px">HOME</span>
    <span class="nav-link abs" style="left:372px">ABOUT US</span>
    <span class="nav-link abs" style="left:476px">SERVICES</span>
    <span class="nav-link abs" style="left:577px">PORTFOLIO</span>
  </nav>
  <div class="btn-contact-nav abs">CONTACT US</div>
  <div class="header-mail abs">
    <svg width="24" height="18" viewBox="0 0 24 18"><rect x="1" y="1" width="22" height="16" fill="none" stroke="#0e4fa1" stroke-width="2"/><path d="M1 1 L12 10 L23 1" fill="none" stroke="#0e4fa1" stroke-width="2"/></svg>
    sample@email.com
  </div>
  <div class="social abs"><span></span><span></span><span></span><span></span></div>
</header>

<section class="hero abs" role="img" aria-label="Engineer in a hard hat beside a steel offshore platform structure over the sea"></section>
<div class="hero-fade abs"></div>
<h1 class="hero-title abs">Lorem Ipsum Dolor</h1>
<p class="hero-text abs">Lorem Ipsum is simply dummy text of the printing and typesetting industry. Lorem Ipsum has been the industry's standard dummy text ever since the 1500s</p>
<div class="btn btn-outline abs">SERVICES</div>
<div class="btn btn-fill abs">CONTACT US</div>
<svg class="arrow abs" style="left:50px" viewBox="0 0 50 50"><path d="M32 8 L14 25 L32 42 M14 25 H46" fill="none" stroke="#fff" stroke-width="3"/></svg>
<svg class="arrow abs" style="left:1100px" viewBox="0 0 50 50"><path d="M18 8 L36 25 L18 42 M36 25 H4" fill="none" stroke="#fff" stroke-width="3"/></svg>

<h2 class="section-title abs" style="top:757px">OUR SERVICES</h2>
<article class="service-card abs" style="left:40px">
  <div class="service-photo" role="img" aria-label="Refinery lit at night" style="background:linear-gradient(160deg,#0b2d6b,#2f6fc4 60%,#0d2a55)"></div>
  <h3 class="service-name">SERVICES NAME</h3>
  <p class="service-text">Lorem Ipsum is simply dummy text of the printing and typesetting industry. Lorem Ipsum has been the industry's standard dummy text ever since the 1500s</p>
</article>
<article class="service-card abs" style="left:323px">
  <div class="service-photo" role="img" aria-label="Yellow offshore rig under blue sky" style="background:linear-gradient(170deg,#3f86d0,#8bb8e0 45%,#d9c23a 70%,#8f7a2a)"></div>
  <h3 class="service-name">SERVICES NAME</h3>
  <p class="service-text">Lorem Ipsum is simply dummy text of the printing and typesetting industry. Lorem Ipsum has been the industry's standard dummy text ever since the 1500s</p>
</article>
<article class="service-card abs" style="left:605px">
  <div class="service-photo" role="img" aria-label="Industrial plant at sunset" style="background:linear-gradient(170deg,#e6b65a,#f1d89a 35%,#8b7a66 70%,#4a4a4e)"></div>
  <h3 class="service-name">SERVICES NAME</h3>
  <p class="service-text">Lorem Ipsum is simply dummy text of the printing and typesetting industry. Lorem Ipsum has been the industry's standard dummy text ever since the 1500s</p>
</article>
<article class="service-card abs" style="left:887px">
  <div class="service-photo" role="img" aria-label="Offshore oil platform at sea" style="background:linear-gradient(175deg,#c9d8e6,#e5e2d4 45%,#c7a56a 70%,#6d8fa8)"></div>
  <h3 class="service-name">SERVICES NAME</h3>
  <p class="service-text">Lorem Ipsum is simply dummy text of the printing and typesetting industry. Lorem Ipsum has been the industry's standard dummy text ever since the 1500s</p>
</article>
<div class="btn-more abs">VIEW MORE</div>

<section class="who-band abs" role="img" aria-label="Blue-toned background of a business meeting"></section>
<h2 class="section-title light abs" style="top:1443px">WHO WE ARE</h2>
<article class="who-card abs" style="left:40px;width:365px">
  <h3 class="who-head">ABOUT US</h3>
  <p class="who-text">Lorem Ipsum is simply dummy text of the printing and typesetting industry. Lorem Ipsum has been the industry's standard dummy text ever since the 1500s Lorem Ipsum is simply dummy text of the printing and typesetting industry. Lorem Ipsum has been the industry's standard dummy text ever since the 1500s</p>
</article>
<article class="who-card abs" style="left:418px;width:363px">
  <h3 class="who-head">OUR MISSION</h3>
  <p class="who-text">Our mission is to provide responsive and unrivalled professional advice from learned and experienced professionals versed in the local market, with an understanding of the cultural and logistical challenges faced by foreign investors.</p>
</article>
<article class="who-card abs" style="left:794px;width:363px">
  <h3 class="who-head">OUR VISION</h3>
  <p class="who-text">Our vision is to provide a complete investor's package that initiates with company registration, compliance and documentation services and ultimately operational facilitation services.</p>
</article>

<h2 class="section-title abs" style="top:1957px">OUR CUSTOMERS FEEDBACK</h2>
<article class="feedback-card abs" style="left:40px">
  <div class="feedback-photo" role="img" aria-label="Portrait of a smiling customer" style="background:linear-gradient(135deg,#cfc7bf,#9c8777 50%,#e9e5e0)"></div>
  <p class="quote">"Lorem Ipsum is simply dummy text of the printing and typesetting industry. Lorem Ipsum has been the industry's standard dummy text ever since the 1500s,"</p>
  <div class="stars"><svg width="108" height="20" viewBox="0 0 108 20"><g fill="#f7941d"><path id="s" d="M10 1 L12.6 7 L19 7.4 L14 11.6 L15.6 18 L10 14.5 L4.4 18 L6 11.6 L1 7.4 L7.4 7Z"/><use href="#s" x="22"/><use href="#s" x="44"/><use href="#s" x="66"/><use href="#s" x="88"/></g></svg></div>
  <p class="person">John Doe<em>Miami, FL</em></p>
</article>
<article class="feedback-card abs" style="left:418px">
  <div class="feedback-photo" role="img" aria-label="Portrait of a smiling customer" style="background:linear-gradient(135deg,#e8e4dc,#c9ad8a 50%,#dcdfe2)"></div>
  <p class="quote">"Lorem Ipsum is simply dummy text of the printing and typesetting industry. Lorem Ipsum has been the industry's standard dummy text ever since the 1500s,"</p>
  <div class="stars"><svg width="108" height="20" viewBox="0 0 108 20"><g fill="#f7941d"><use href="#s"/><use href="#s" x="22"/><use href="#s" x="44"/><use href="#s" x="66"/><use href="#s" x="88"/></g></svg></div>
  <p class="person">Jane Doe<em>Santa Monica, CA</em></p>
</article>
<article class="feedback-card abs" style="left:794px">
  <div class="feedback-photo" role="img" aria-label="Portrait of a smiling customer" style="background:linear-gradient(135deg,#9aa6b2,#c9ab86 50%,#7e8b97)"></div>
  <p class="quote">"Lorem Ipsum is simply dummy text of the printing and typesetting industry. Lorem Ipsum has been the industry's standard dummy text ever since the 1500s,"</p>
  <div class="stars"><svg width="108" height="20" viewBox="0 0 108 20"><g fill="#f7941d"><use href="#s"/><use href="#s" x="22"/><use href="#s" x="44"/><use href="#s" x="66"/><use href="#s" x="88"/></g></svg></div>
  <p class="person">Jack Doe<em>San Francisco, CA</em></p>
</article>
<svg class="abs" style="left:48px;top:2225px" width="30" height="44" viewBox="0 0 30 44"><path d="M24 4 L6 22 L24 40" fill="none" stroke="#fff" stroke-width="3"/></svg>
<svg class="abs" style="left:1122px;top:2225px" width="30" height="44" viewBox="0 0 30 44"><path d="M6 4 L24 22 L6 40" fill="none" stroke="#fff" stroke-width="3"/></svg>

<section class="contact-band abs" role="img" aria-label="Blue-toned industrial plant and workspace background"></section>
<h2 class="section-title light abs" style="top:2589px">GET IN TOUCH</h2>
<div class="form-panel abs">
  <h3 class="form-title abs">Send us a message</h3>
  <svg class="abs" style="left:484px;top:48px" width="52" height="34" viewBox="0 0 52 34"><g fill="none" stroke="#f7941d" stroke-width="2"><rect x="14" y="3" width="36" height="28"/><path d="M14 3 L32 18 L50 3"/><path d="M2 10 H10 M5 17 H10 M2 24 H10"/></g></svg>
  <div class="field abs" style="left:56px;top:134px">Enter your name</div>
  <div class="field abs" style="left:323px;top:134px">Enter your email</div>
  <div class="field abs" style="left:56px;top:232px">Enter your subject</div>
  <div class="field abs" style="left:323px;top:232px">Enter your phone number</div>
  <div class="field abs" style="left:56px;top:330px">Enter your message</div>
  <div class="send abs"><svg width="104" height="56" viewBox="0 0 104 56"><path d="M38 29 L66 17 L58 42 L51 32 Z M51 32 L66 17" fill="none" stroke="#fff" stroke-width="2.2" stroke-linejoin="round"/></svg></div>
</div>
<div class="info-panel abs">
  <h3 class="info-title abs">Contact Information</h3>
  <div class="info-row abs" style="top:126px">
    <svg width="42" height="46" viewBox="0 0 42 46"><g fill="none" stroke="#fff" stroke-width="2"><path d="M21 34 C12 22 10 19 10 14 A11 11 0 0 1 32 14 C32 19 30 22 21 34Z"/><circle cx="21" cy="14" r="4"/><path d="M12 30 L3 42 H39 L30 30"/></g></svg>
    <span>1234 Sample Address<br>Sample city</span>
  </div>
  <div class="info-row abs" style="top:204px">
    <svg width="42" height="40" viewBox="0 0 42 40"><g fill="none" stroke="#fff" stroke-width="2"><rect x="3" y="8" width="36" height="28"/><path d="M3 8 L21 24 L39 8"/><circle cx="21" cy="10" r="6"/></g></svg>
    <span>sample@email.com</span>
  </div>
  <div class="info-row abs" style="top:276px">
    <svg width="42" height="42" viewBox="0 0 42 42"><path d="M8 3 L15 3 L18 12 L13 16 C16 23 20 27 27 30 L31 25 L40 28 L40 35 C40 38 37 40 34 40 C18 38 4 24 3 9 C3 6 5 3 8 3Z" fill="none" stroke="#fff" stroke-width="2"/></svg>
    <span>12345-567-34343</span>
  </div>
  <div class="info-social abs"><span></span><span></span><span></span><span></span></div>
</div>

<footer>
  <div class="footer-brand abs"><span class="brand-mark"></span><span class="brand-name">MARENDO</span></div>
  <p class="copyright abs">Copyright © 218 - Marendo Adviser</p>
</footer>

</body>
</html>
```